Home page design for a live auction website.

Hi, we are looking at finding a good design for an auction website, only home page .. We will not be selling anything online, so the website will only be a portal where visitors can check about our company, upcoming auctions, online catalogues etc.
See attached our logo. Please use the same red that you see on the logo in the designs that you provide.
The final design should communicate high-end auction website, as we will be selling expensive piece of arts and antiques.
We should have a main frame where images of arts will circulate, with description of the art piece. just like on http://paris.vellmarotte-quisande.com/
(but with a better design overall) and of course a menu with different tabs, like "about us", "previous sales" "next sales", "contact" , "how to buy", "meet our specialists".

Target Market(s)

High end segment, who can afford to pay up to 250'000 for a piece of art

Industry/Entity Type

Online

Number of Pages Required

1 page

Requirements
Must have
• a frame with images rotating, just like on http://paris.vellmarotte-quisande.com/ . but the rest of the design should be more refined.
• we should also have a strong call to action, "Free online estimation", click here, estimation delivered in 48 hours"
Nice to have
• Tremaux Auctions, the brand should be well visible

```html
<!DOCTYPE html>
<html lang="en">
<head>
<meta charset="utf-8">
<title>Tremaux Auctions — Home</title>
<link href="https://fonts.googleapis.com/css2?family=Open+Sans:wght@400;600;700;800&family=Roboto+Condensed:wght@400;700&display=swap" rel="stylesheet">
<style>
:root{
  --red:#c4161c;
  --red-dark:#9e1015;
  --ink:#2b2b2b;
  --muted:#777;
  --line:#e2e2e2;
  --paper:#fff;
  --soft:#f3f3f3;
  --dark:#262a2e;
  --darker:#1b1e21;
  --gold:#e7b64a;
}
*{box-sizing:border-box;margin:0;padding:0}
html,body{width:1200px;height:3980px;overflow:hidden}
body{font-family:"Open Sans",Arial,sans-serif;color:var(--ink);background:var(--paper);font-size:12px;line-height:1.55}
.page{position:relative;width:1200px;height:3980px}
.wrap{width:920px;margin:0 auto;position:relative}

/* top bar */
.topbar{height:24px;background:#333;color:#ccc;font-size:10px;display:flex;align-items:center;justify-content:space-between;padding:0 140px 0 140px}
.topbar .links{display:flex;height:24px;align-items:center;gap:14px}
.topbar .links .tag{background:var(--red);color:#fff;height:24px;line-height:24px;padding:0 12px;font-weight:700}

/* header */
.header{height:96px;display:flex;align-items:center;justify-content:space-between;padding:0 140px;border-bottom:1px solid var(--line)}
.brand{display:flex;align-items:center;gap:10px;font-size:20px;font-weight:700;color:var(--red);letter-spacing:.5px}
.brand .mark{width:14px;height:14px;background:var(--red)}
.nav{display:flex;gap:4px;font-size:10.5px;font-weight:600;text-transform:uppercase}
.nav a{padding:10px 12px;color:#444;text-decoration:none}
.nav a.active{background:var(--red);color:#fff}

/* hero */
.hero{position:relative;height:592px;background:radial-gradient(ellipse at 60% 45%,#3b4a4a 0%,#1d2526 60%,#111617 100%);overflow:hidden;color:#fff}
.hero .piece{position:absolute;left:70px;top:40px;width:210px;height:500px;border-radius:90px 90px 40px 40px;background:linear-gradient(180deg,#3a2a1c,#7a3a1c 35%,#b3572a 60%,#5a2a16)}
.hero .caption{position:absolute;left:300px;top:190px;width:240px}
.hero .caption h2{font-family:"Roboto Condensed",sans-serif;font-size:26px;color:var(--gold);font-weight:700}
.hero .caption .cat{font-size:11px;color:#bbb;margin-bottom:14px}
.hero .caption p{font-size:11px;color:#ddd;margin-bottom:18px}
.hero .price{display:inline-block;background:var(--paper);color:var(--ink);font-weight:700;padding:6px 14px;border-radius:3px;font-size:12px}
.cta-title{position:absolute;left:640px;top:56px;width:520px;text-align:center;font-family:"Roboto Condensed",sans-serif;font-size:34px;font-weight:700;letter-spacing:1px}
.clock{position:absolute;left:660px;top:120px;width:480px;height:480px;border-radius:50%;background:radial-gradient(circle,#c9b27a 0%,#8a6f3a 45%,#3a2e1a 75%,#1d1710 100%);box-shadow:0 0 0 10px #2b2216}
.clock-text{position:absolute;left:660px;top:300px;width:480px;text-align:center;font-family:"Roboto Condensed",sans-serif;color:#fff;text-shadow:0 2px 4px rgba(0,0,0,.6)}
.clock-text .a{font-size:24px;font-weight:700;letter-spacing:2px}
.clock-text .b{font-size:48px;font-weight:700;line-height:1.1}
.clock-text .btn{display:inline-block;margin-top:14px;background:var(--red);padding:8px 22px;font-size:15px;font-weight:700;border-radius:3px;text-shadow:none}
.arrow{position:absolute;top:280px;width:28px;height:28px;border-radius:50%;background:rgba(255,255,255,.25)}
.arrow.l{left:14px}.arrow.r{right:14px}
.dots{position:absolute;bottom:22px;left:0;right:0;display:flex;justify-content:center;gap:10px}
.dots i{width:12px;height:12px;border-radius:50%;background:#777;display:block}
.dots i.on{background:var(--paper)}

/* headings */
.sec-title{text-align:center}
.sec-title h3{font-size:17px;font-weight:800;letter-spacing:.5px;text-transform:uppercase}
.sec-title h3 em{font-style:normal;color:var(--red)}
.sec-title .sub{font-size:10px;color:var(--muted)}
.sec-title .bar{width:60px;height:2px;background:var(--red);margin:6px auto 0}
.intro{font-size:11px;color:var(--muted);text-align:center;margin-top:18px}

.welcome{padding-top:34px;height:200px}
.welcome .rule{position:absolute;top:-18px;left:0;right:0;height:1px;background:var(--line)}

/* sales */
.sales{position:relative;height:420px}
.tab-head{position:relative;height:56px;border-bottom:1px solid var(--line);margin:0 20px 0 0}
.tab-head .cap{position:absolute;left:140px;top:8px;width:42px;height:48px;background:var(--red);color:#fff;font-size:34px;font-weight:800;text-align:center;line-height:48px}
.tab-head .rest{position:absolute;left:186px;top:24px;font-size:20px;font-weight:800;text-transform:uppercase}
.tab-head .ctrl{position:absolute;right:120px;top:26px;display:flex;gap:6px}
.tab-head .ctrl i{width:18px;height:18px;background:#ddd;display:block}
.tab-head .ctrl i.on{background:#444}
.cards{display:flex;gap:20px;margin-top:26px}
.card{width:215px;background:var(--paper);border:1px solid var(--line);box-shadow:0 2px 6px rgba(0,0,0,.08);padding:14px 14px 12px}
.card .img{height:150px;border-radius:2px}
.card h4{font-size:14px;font-weight:800;text-align:center;margin-top:10px}
.card p{font-size:10px;color:var(--muted);text-align:center;margin-top:4px;height:48px}
.card .price{display:flex;align-items:center;margin-top:6px;font-size:11px;font-weight:700}
.card .price b{background:var(--red);color:#fff;padding:3px 8px;font-size:10px}
.card .price span{border:1px solid var(--line);padding:2px 10px}

/* specialists */
.specialists{height:610px;padding-top:10px}
.spec-cards{display:flex;gap:30px;justify-content:center;margin-top:50px}
.spec{width:260px;background:var(--paper);border:1px solid var(--line);box-shadow:0 2px 8px rgba(0,0,0,.1);padding:24px 20px;text-align:center}
.spec .avatar{width:120px;height:130px;margin:0 auto;background:linear-gradient(180deg,#e6e6e6,#bdbdbd);border-radius:4px}
.spec h5{font-size:14px;font-weight:800;margin-top:14px}
.spec .cat{font-size:10px;color:var(--muted)}
.spec p{font-size:10px;color:var(--muted);margin-top:10px}
.social{display:flex;gap:5px;justify-content:center;margin-top:14px}
.social i{width:18px;height:18px;display:block;background:#555}
.social i:nth-child(2){background:#777}.social i:nth-child(3){background:#999}

/* how to buy */
.howto{height:470px;border-top:1px solid var(--line);position:relative}
.ribbon{position:absolute;left:520px;top:-18px;width:160px;height:40px;background:var(--red);color:#fff;font-family:"Roboto Condensed",sans-serif;font-size:20px;font-weight:700;text-align:center;line-height:40px}
.ribbon:before,.ribbon:after{content:"";position:absolute;top:8px;width:26px;height:40px;background:var(--red-dark);z-index:-1}
.ribbon:before{left:-18px}.ribbon:after{right:-18px}
.howto .photo{position:absolute;left:160px;top:110px;width:200px;height:260px;background:linear-gradient(180deg,#f5f5f5,#c9c9c9 55%,#3a3a3a);border-radius:4px}
.steps{position:absolute;left:380px;top:118px;width:680px}
.step{display:flex;align-items:stretch;background:var(--soft);margin-bottom:4px;font-size:9.5px;text-transform:uppercase;color:#555}
.step .n{width:26px;background:#555;color:#fff;text-align:center;line-height:26px;font-weight:700}
.step .t{padding:0 10px;line-height:26px}
.step.open{flex-wrap:wrap;background:transparent}
.step.open .t{background:var(--soft);flex:1}
.step.open p{width:100%;text-transform:none;font-size:10px;color:var(--muted);padding:10px 0 10px 36px}

/* contact */
.contact{height:336px;background:var(--soft);padding-top:28px}
.contact .cols{display:flex;margin-top:30px;gap:40px}
.contact .info{width:160px;font-size:10px}
.contact .info b{display:block;font-size:10px;font-weight:800;margin-top:10px}
.contact .form{flex:1;padding-left:70px}
.row{display:flex;gap:10px;margin-bottom:10px}
.field{flex:1;height:28px;background:var(--paper);border:1px solid var(--line)}
.field.area{height:96px}
.submit{display:inline-block;background:var(--red);color:#fff;font-size:10px;font-weight:700;padding:7px 16px}

/* map */
.map{height:372px;background:linear-gradient(135deg,#dfe6d9,#cfd9e4 40%,#e6e2d6 70%,#d5dfcf)}

/* footer */
.footer{height:348px;background:var(--dark);color:#aaa;padding-top:36px}
.footer .cols{display:flex;gap:30px}
.footer .col{width:210px;font-size:10px}
.footer h6{color:#fff;font-size:13px;font-weight:700;text-transform:uppercase;margin-bottom:14px}
.footer .brand{color:var(--paper);font-size:16px;margin-bottom:12px}
.footer .brand .mark{background:var(--red)}
.news{display:flex;margin-top:8px}
.news .in{flex:1;height:24px;background:#3a3f44}
.news .go{width:30px;height:24px;background:#555}
.tw{display:flex;gap:8px;margin-bottom:12px}
.tw i{width:12px;height:12px;border-radius:50%;background:#4a9fd8;flex:none;margin-top:2px}
.blog{display:flex;gap:8px;margin-bottom:12px}
.blog .th{width:40px;height:40px;background:linear-gradient(135deg,#6a5a44,#3a3028);flex:none}
.gallery{display:grid;grid-template-columns:repeat(3,56px);gap:6px}
.gallery i{height:56px;display:block;background:linear-gradient(135deg,#7a6a52,#3a3128)}
.copyright{height:40px;background:var(--darker);color:#888;font-size:10px;text-align:center;line-height:40px}
.copyright em{color:var(--red);font-style:normal}
</style>
</head>
<body>
<div class="page">

  <div class="topbar">
    <span>support@tremauxauctions.com</span>
    <div class="links"><span class="tag">AUCTIONS</span><span>SIGN IN ACCOUNT</span><span>SIGN UP</span><span>LOGIN</span></div>
  </div>

  <header class="header">
    <div class="brand"><span class="mark"></span>Tremaux Auctions</div>
    <nav class="nav">
      <a class="active">Home</a><a>About Us</a><a>Previous Sales</a><a>Next Sales</a><a>Meet Our Specialists</a><a>How To Buy</a><a>Contact</a>
    </nav>
  </header>

  <section class="hero">
    <div class="piece" role="img" aria-label="Hand-painted antique floral vase with handle"></div>
    <div class="caption">
      <h2>Antique Vase #01</h2>
      <div class="cat">Category: Ceramics</div>
      <p>Lorem ipsum is simply dummy text of the printing and typesetting industry. Lorem ipsum has been the standard.</p>
      <span class="price">7,500 $</span>
    </div>
    <div class="cta-title">FREE ONLINE ESTIMATION</div>
    <div class="clock" role="img" aria-label="Large antique clock face"></div>
    <div class="clock-text">
      <div class="a">ESTIMATION DELIVERED</div>
      <div class="b">IN 48 HOURS</div>
      <span class="btn">Click Here</span>
    </div>
    <span class="arrow l"></span><span class="arrow r"></span>
    <div class="dots"><i></i><i class="on"></i><i></i><i></i><i></i></div>
  </section>

  <section class="welcome wrap">
    <div class="sec-title">
      <h3>Welcome to <em>Tremaux Auctions</em></h3>
      <div class="sub">About Us</div>
      <div class="bar"></div>
    </div>
    <p class="intro">Lorem ipsum is simply dummy text of the printing and typesetting industry. Lorem ipsum has been the industry's standard dummy text ever since the 1500s, when an unknown printer took a galley of type and scrambled it to make a type specimen book. It has survived not only five centuries, but also the leap into electronic typesetting, remaining essentially unchanged. It was popularised with the release of sheets containing passages, and more recently with desktop publishing software including versions of it.</p>
  </section>

  <section class="sales">
    <div class="tab-head"><span class="cap">P</span><span class="rest">revious Sales</span><span class="ctrl"><i></i><i class="on"></i></span></div>
    <div class="wrap cards">
      <div class="card"><div class="img" role="img" aria-label="Antique gramophone" style="background:linear-gradient(180deg,#efe9df,#8a6a3c)"></div><h4>ITEM #056</h4><p>Lorem ipsum is simply dummy text of the printing and typesetting industry.</p><div class="price"><b>PRICE</b><span>$ 750.00</span></div></div>
      <div class="card"><div class="img" role="img" aria-label="Framed old map" style="background:linear-gradient(135deg,#a08a5a,#6b5a34)"></div><h4>ITEM #224</h4><p>Lorem ipsum is simply dummy text of the printing and typesetting industry.</p><div class="price"><b>PRICE</b><span>$ 4,400.00</span></div></div>
      <div class="card"><div class="img" role="img" aria-label="Ancient bronze helmet" style="background:linear-gradient(180deg,#f2f2f2,#9a7a48)"></div><h4>ITEM #014</h4><p>Lorem ipsum is simply dummy text of the printing and typesetting industry.</p><div class="price"><b>PRICE</b><span>$ 750.00</span></div></div>
      <div class="card"><div class="img" role="img" aria-label="Antique world map" style="background:linear-gradient(135deg,#c7b48a,#8a7a52)"></div><h4>ITEM #054</h4><p>Lorem ipsum is simply dummy text of the printing and typesetting industry.</p><div class="price"><b>PRICE</b><span>$ 900.00</span></div></div>
    </div>
  </section>

  <section class="sales">
    <div class="tab-head"><span class="cap">N</span><span class="rest">ext Sales</span><span class="ctrl"><i></i><i class="on"></i></span></div>
    <div class="wrap cards">
      <div class="card"><div class="img" role="img" aria-label="Bronze horse and rider sculpture" style="background:linear-gradient(180deg,#f4f4f4,#4a3a2c)"></div><h4>ITEM #094</h4><p>Lorem ipsum is simply dummy text of the printing and typesetting industry.</p><div class="price"><b>PRICE</b><span>$ 700.00</span></div></div>
      <div class="card"><div class="img" role="img" aria-label="Painted antique vase" style="background:linear-gradient(180deg,#f4f4f4,#7a4a24)"></div><h4>ITEM #01</h4><p>Lorem ipsum is simply dummy text of the printing and typesetting industry.</p><div class="price"><b>PRICE</b><span>$ 500.00</span></div></div>
      <div class="card"><div class="img" role="img" aria-label="Antique longcase clock" style="background:linear-gradient(180deg,#f4f4f4,#5a2e1a)"></div><h4>ITEM #08</h4><p>Lorem ipsum is simply dummy text of the printing and typesetting industry.</p><div class="price"><b>PRICE</b><span>$ 250.00</span></div></div>
      <div class="card"><div class="img" role="img" aria-label="Framed painting of a decorated elephant" style="background:linear-gradient(135deg,#c9a04a,#7a2a1a)"></div><h4>ITEM #054</h4><p>Lorem ipsum is simply dummy text of the printing and typesetting industry.</p><div class="price"><b>PRICE</b><span>$ 900.00</span></div></div>
    </div>
  </section>

  <section class="specialists wrap">
    <div class="sec-title">
      <h3>Meet Our <em>Specialists</em></h3>
      <div class="sub">Guidance</div>
      <div class="bar"></div>
    </div>
    <p class="intro">Lorem ipsum is simply dummy text of the printing and typesetting industry. Lorem ipsum has been the industry's standard dummy text ever since the 1500s, when an unknown printer took a galley of type and scrambled it to make a type specimen book. It has survived not only five centuries, but also the leap into electronic typesetting, remaining unchanged.</p>
    <div class="spec-cards">
      <div class="spec"><div class="avatar" role="img" aria-label="Specialist portrait placeholder"></div><h5>Specialist</h5><div class="cat">Category</div><p>Lorem ipsum is simply dummy text of the printing and typesetting industry, standard dummy text ever since.</p><div class="social"><i></i><i></i><i></i><i></i></div></div>
      <div class="spec"><div class="avatar" role="img" aria-label="Specialist portrait placeholder"></div><h5>Specialist</h5><div class="cat">Category</div><p>Lorem ipsum is simply dummy text of the printing and typesetting industry, standard dummy text ever since.</p><div class="social"><i></i><i></i><i></i><i></i></div></div>
      <div class="spec"><div class="avatar" role="img" aria-label="Specialist portrait placeholder"></div><h5>Specialist</h5><div class="cat">Category</div><p>Lorem ipsum is simply dummy text of the printing and typesetting industry, standard dummy text ever since.</p><div class="social"><i></i><i></i><i></i><i></i></div></div>
    </div>
  </section>

  <section class="howto">
    <div class="ribbon">HOW TO BUY</div>
    <div class="photo" role="img" aria-label="Cheerful woman seated with a laptop"></div>
    <div class="steps">
      <div class="step open"><span class="n">1</span><span class="t">Login or Register</span><p>Lorem ipsum is simply dummy text of the printing and typesetting industry. Lorem ipsum has been the industry's standard dummy text ever since the 1500s, when an unknown printer took a galley of type and scrambled it to make a type specimen book. It has survived five centuries, and the leap into electronic typesetting, remaining essentially unchanged for bidders.</p></div>
      <div class="step"><span class="n">2</span><span class="t">Browse the catalogue and select your lots</span></div>
      <div class="step"><span class="n">3</span><span class="t">Request a condition report from our specialists</span></div>
      <div class="step"><span class="n">4</span><span class="t">Place your bid in the room or by phone</span></div>
      <div class="step"><span class="n">5</span><span class="t">Settle payment and arrange delivery</span></div>
      <div class="step"><span class="n">6</span><span class="t">Receive your piece with full documentation</span></div>
    </div>
  </section>

  <section class="contact">
    <div class="wrap">
      <div class="sec-title">
        <h3>Contact Us</h3>
        <div class="sub">We would love to hear from you</div>
      </div>
      <div class="cols">
        <div class="info"><b>EMAIL</b>support@tremauxauctions.com<b>PHONE</b>+41 22 555 0148<b>SOCIAL MEDIA</b><div class="social" style="justify-content:flex-start"><i></i><i></i><i></i><i></i></div></div>
        <div class="info"><b>ADDRESS</b>Geneva<br>14 Rue Delmarre</div>
        <div class="form">
          <div class="row"><span class="field"></span><span class="field"></span></div>
          <div class="row"><span class="field area"></span></div>
          <span class="submit">SUBMIT</span>
        </div>
      </div>
    </div>
  </section>

  <div class="map" role="img" aria-label="Street map showing the Tremaux Auctions location"></div>

  <footer class="footer">
    <div class="wrap cols">
      <div class="col">
        <div class="brand"><span class="mark"></span>Tremaux Auctions</div>
        <p>Lorem ipsum is simply dummy text of the printing and typesetting industry, standard dummy text ever since the 1500s.</p>
        <h6 style="margin-top:20px">Newsletter</h6>
        <div class="news"><span class="in"></span><span class="go"></span></div>
      </div>
      <div class="col">
        <h6>Latest Twittes</h6>
        <div class="tw"><i></i><span>Lorem ipsum is simply dummy text of the printing industry.</span></div>
        <div class="tw"><i></i><span>Lorem ipsum is simply dummy text of the printing industry.</span></div>
        <div class="tw"><i></i><span>Lorem ipsum is simply dummy text of the printing industry.</span></div>
      </div>
      <div class="col">
        <h6>Latest Blog</h6>
        <div class="blog"><span class="th" role="img" aria-label="Blog thumbnail"></span><span>Lorem ipsum is simply dummy text of the printing.</span></div>
        <div class="blog"><span class="th" role="img" aria-label="Blog thumbnail"></span><span>Lorem ipsum is simply dummy text of the printing.</span></div>
        <div class="blog"><span class="th" role="img" aria-label="Blog thumbnail"></span><span>Lorem ipsum is simply dummy text of the printing.</span></div>
      </div>
      <div class="col">
        <h6>Auction Gallery</h6>
        <div class="gallery" role="img" aria-label="Grid of auction lot thumbnails"><i></i><i></i><i></i><i></i><i></i><i></i><i></i><i></i><i></i></div>
      </div>
    </div>
  </footer>
  <div class="copyright">Copyright 2015 All Rights Reserved <em>Tremaux Auctions</em> | Privacy Policy | Terms &amp; Conditions</div>

</div>
</body>
</html>
```